Employee Portal UI Design - Modern and Clean

We are an agency tasked with developing a team portal for a company that has many employees. As we embark on this project, we seek a great UI design to accompany the requirements our client has for this project. We already have several screens mocked up that can be used as reference for the overall idea. Currently, we are only looking for the main dashboard's home page, user registration screen, and account settings page to be designed. The main brand colors are red but other accents can be used as well. The client's vision is for modern & minimalist to be at the center. We have a specific font to be used, but if you don't have access to it, you can just use a similar font.Main color: #DD0031The sub menus (do not need to be designed) would be:>Performance Reviews>Posts>Team directory>Calendar>Tasks>Documents>LinksWe would prefer the design be made in Adobe XD.

Industry/Entity Type

Fast Food Restaurant

Number of Pages Required

1 page

Font styles to use
Sans Serif

Colors
ec1f27

Requirements
Must have
• Color: #DD0031 (highlights)

```html
<!DOCTYPE html>
<html lang="en">
<head>
<meta charset="UTF-8">
<title>Crewdash – Home</title>
<link href="https://fonts.googleapis.com/css2?family=Barlow:wght@400;500;600;700&display=swap" rel="stylesheet">
<style>
  :root{
    --brand:#ec1f27;
    --brand-deep:#dd0031;
    --ink:#2e2e2e;
    --text:#555;
    --muted:#9a9a9a;
    --line:#e3e3e3;
    --canvas:#f3f3f3;
    --panel:#ffffff;
    --nav-active:#4b4b4b;
    --accent-blue:#1a73e8;
    --avatar:#8a7a6c;
  }
  *{box-sizing:border-box;margin:0;padding:0}
  html,body{width:1200px;height:800px;overflow:hidden}
  body{font-family:"Barlow",sans-serif;color:var(--text);background:var(--panel);display:flex}

  /* Sidebar */
  .sidebar{width:238px;height:800px;background:var(--panel);border-right:1px solid var(--line);flex-shrink:0}
  .brand{height:88px;display:flex;align-items:center;padding-left:28px;border-bottom:1px solid var(--line)}
  .brand-name{font-size:42px;font-weight:400;color:var(--ink);letter-spacing:.5px}
  .user{height:98px;display:flex;align-items:center;padding-left:30px;gap:12px}
  .avatar{border-radius:50%;background:radial-gradient(circle at 50% 40%,#b9a592,var(--avatar) 70%,#4e4540);flex-shrink:0}
  .avatar-lg{width:66px;height:66px}
  .user-name{font-size:15px;color:var(--text);display:flex;align-items:center;gap:8px}
  .caret{width:0;height:0;border-left:5px solid transparent;border-right:5px solid transparent;border-top:6px solid var(--ink)}
  .nav{list-style:none}
  .nav-item{height:57px;display:flex;align-items:center;gap:14px;padding-left:30px;font-size:14px;color:var(--text);border-left:4px solid transparent}
  .nav-item svg{width:18px;height:18px;fill:var(--ink)}
  .nav-item.is-active{background:var(--nav-active);color:#fff;border-left-color:var(--brand)}
  .nav-item.is-active svg{fill:#fff}

  /* Main */
  .main{flex:1;display:flex;flex-direction:column}
  .topbar{height:88px;background:var(--brand);display:flex;align-items:center;padding:0 30px 0 26px;gap:22px}
  .icon-btn{width:30px;height:30px;fill:#fff}
  .search{width:280px;height:38px;border-radius:19px;background:#fff;display:flex;align-items:center;gap:8px;padding-left:12px;font-size:13px;color:var(--muted)}
  .search svg{width:20px;height:20px;stroke:var(--muted);fill:none;stroke-width:2}
  .topbar-actions{margin-left:auto;display:flex;gap:30px;align-items:center}

  .content{flex:1;background:var(--canvas);display:flex;gap:22px;padding:20px 28px 20px 26px}
  .activities{flex:1;display:flex;flex-direction:column}
  .section-head{display:flex;justify-content:space-between;align-items:center;height:40px;margin-bottom:8px}
  .section-title{font-size:18px;color:var(--ink);font-weight:400}
  .btn{background:var(--brand);color:#fff;border-radius:16px;font-size:12px;font-weight:500;display:inline-flex;align-items:center;justify-content:center;gap:14px}
  .btn-new{height:32px;padding:0 16px 0 22px}
  .post{background:var(--panel);border:1px solid var(--line);border-radius:4px;box-shadow:0 1px 4px rgba(0,0,0,.08);padding:16px 20px 18px 20px;margin-bottom:18px;height:189px}
  .post:last-child{margin-bottom:0}
  .post-head{display:flex;align-items:center;height:40px;margin-bottom:14px}
  .avatar-sm{width:36px;height:36px;margin-right:8px}
  .author{padding-right:14px;border-right:1px solid var(--line);line-height:1.1}
  .author-name{color:var(--brand);font-size:14px}
  .author-scope{font-size:10px;font-weight:700;color:var(--ink)}
  .post-subject{padding-left:14px;font-size:14px;color:var(--text)}
  .post-time{margin-left:auto;font-size:10px;font-weight:600;color:var(--ink);display:flex;align-items:center;gap:5px}
  .post-time svg{width:11px;height:11px;stroke:var(--muted);fill:none}
  .post-body{font-size:13.5px;line-height:25px;color:var(--text)}
  .read-more{color:var(--brand);font-weight:600;margin-left:8px}

  .aside{width:228px;display:flex;flex-direction:column}
  .card{background:var(--panel);border:1px solid var(--line);border-radius:3px;box-shadow:0 1px 4px rgba(0,0,0,.08)}
  .tabs{display:flex;height:50px;border-bottom:1px solid var(--line)}
  .tab{flex:1;display:flex;align-items:center;justify-content:center;font-size:17px;color:var(--muted)}
  .tab.is-active{color:var(--ink);border-bottom:2px solid var(--brand)}
  .events{padding:0 18px}
  .event{padding:12px 0 10px;border-bottom:1px solid var(--line)}
  .event-title{font-size:14px;display:flex;align-items:center;gap:8px}
  .dot{width:7px;height:7px;border-radius:50%}
  .event-red .event-title{color:var(--brand)} .event-red .dot{background:var(--brand)}
  .event-blue .event-title{color:var(--accent-blue)} .event-blue .dot{background:var(--accent-blue)}
  .event-meta{font-size:9.5px;color:var(--text);padding-left:15px;line-height:16px;margin-top:3px}
  .card-link{display:block;text-align:center;color:var(--brand);font-weight:600;font-size:13.5px;padding:16px 0 14px}
  .polls-title{font-size:17px;color:var(--ink);margin:14px 0 8px}
  .poll{padding:14px 18px 0}
  .poll-q{font-size:10px;color:var(--text);margin-bottom:12px}
  .poll-option{font-size:10px;color:var(--text);padding:5px 0 5px 10px;border-left:3px solid transparent;margin-bottom:8px}
  .poll-option.is-selected{color:var(--brand);font-weight:600;border-left-color:var(--brand)}
  .btn-vote{height:32px;padding:0 16px;font-size:10px;display:flex;width:max-content;margin:10px auto 0}
  .poll .card-link{border-top:1px solid var(--line);margin-top:16px}
</style>
</head>
<body>
  <aside class="sidebar">
    <div class="brand"><span class="brand-name">Crewdash</span></div>
    <div class="user">
      <div class="avatar avatar-lg" role="img" aria-label="Profile photo of Martin Hale"></div>
      <span class="user-name">Martin Hale <span class="caret"></span></span>
    </div>
    <ul class="nav">
      <li class="nav-item is-active"><svg viewBox="0 0 24 24"><path d="M12 3 2 12h3v9h6v-6h2v6h6v-9h3z"/></svg>Home</li>
      <li class="nav-item"><svg viewBox="0 0 24 24"><rect x="3" y="12" width="3" height="9"/><rect x="8" y="8" width="3" height="13"/><rect x="13" y="4" width="3" height="17"/><rect x="18" y="14" width="3" height="7"/></svg>Performance Reviews</li>
      <li class="nav-item"><svg viewBox="0 0 24 24"><path d="M12 2 2 7l10 5 10-5zM2 12l10 5 10-5-2-1-8 4-8-4zm0 5 10 5 10-5-2-1-8 4-8-4z"/></svg>Posts</li>
      <li class="nav-item"><svg viewBox="0 0 24 24"><circle cx="8" cy="8" r="3.5"/><circle cx="16" cy="8" r="3.5"/><path d="M1 19c0-4 3-6 7-6s7 2 7 6zm14 0c0-2-.6-3.6-1.8-4.8C18 13.8 23 15 23 19z"/></svg>Team Directory</li>
      <li class="nav-item"><svg viewBox="0 0 24 24"><path d="M3 5h18v16H3zm2 5v9h14v-9zM7 2h2v4H7zm8 0h2v4h-2z"/></svg>Calendar</li>
      <li class="nav-item"><svg viewBox="0 0 24 24"><path d="M3 5h18v2H3zm0 6h18v2H3zm0 6h18v2H3zM7 3h2v6H7zm8 6h2v6h-2zm-6 6h2v6H9z"/></svg>Tasks</li>
      <li class="nav-item"><svg viewBox="0 0 24 24"><path d="M2 5h8l2 2h10v13H2z"/></svg>Documents</li>
      <li class="nav-item"><svg viewBox="0 0 24 24"><path d="M7 8h4v2H7a2 2 0 0 0 0 4h4v2H7a4 4 0 0 1 0-8zm6 0h4a4 4 0 0 1 0 8h-4v-2h4a2 2 0 0 0 0-4h-4zm-5 3h8v2H8z"/></svg>Links</li>
    </ul>
  </aside>

  <div class="main">
    <header class="topbar">
      <svg class="icon-btn" viewBox="0 0 24 24"><rect x="3" y="5" width="18" height="2"/><rect x="3" y="11" width="18" height="2"/><rect x="3" y="17" width="18" height="2"/></svg>
      <div class="search"><svg viewBox="0 0 24 24"><circle cx="10" cy="10" r="7"/><path d="m15 15 6 6"/></svg>Search</div>
      <div class="topbar-actions">
        <svg class="icon-btn" viewBox="0 0 24 24"><path d="M12 3a6 6 0 0 0-6 6v5l-2 3h16l-2-3V9a6 6 0 0 0-6-6zm-2 16a2 2 0 0 0 4 0z" fill="none" stroke="#fff" stroke-width="1.6"/><circle cx="17" cy="5" r="3"/></svg>
        <svg class="icon-btn" viewBox="0 0 24 24"><path d="M19.4 13a7.5 7.5 0 0 0 0-2l2.1-1.6-2-3.5-2.5 1a7 7 0 0 0-1.7-1L15 3h-4l-.4 2.8a7 7 0 0 0-1.7 1l-2.5-1-2 3.5L6.6 11a7.5 7.5 0 0 0 0 2l-2.1 1.6 2 3.5 2.5-1a7 7 0 0 0 1.7 1L11 21h4l.4-2.8a7 7 0 0 0 1.7-1l2.5 1 2-3.5zM13 15.5a3.5 3.5 0 1 1 0-7 3.5 3.5 0 0 1 0 7z" transform="translate(-1 0)"/></svg>
      </div>
    </header>

    <div class="content">
      <section class="activities">
        <div class="section-head">
          <h2 class="section-title">Recent Activites</h2>
          <span class="btn btn-new">New <span>+</span></span>
        </div>
        <article class="post">
          <div class="post-head">
            <div class="avatar avatar-sm" role="img" aria-label="Profile photo of Martin Hale"></div>
            <div class="author"><div class="author-name">Martin Hale</div><div class="author-scope">Public</div></div>
            <div class="post-subject">Post Subject Message</div>
            <div class="post-time"><svg viewBox="0 0 12 12"><circle cx="6" cy="6" r="5"/><path d="M6 3v3l2 1"/></svg>Today, 1:43</div>
          </div>
          <p class="post-body">Lorem ipsum dolor sit amet, paulo soleat ex sed. Discere perpetua tincidunt mel ea, mel vocent dissentiunt ut, duis aeque mucius vis ex. Eros ipsum causae ex vis, ad eos nostrud ponderum. Ea nonumy accommodare vel, te nullam docendi theophrastus mea.<span class="read-more">Read More</span></p>
        </article>
        <article class="post">
          <div class="post-head">
            <div class="avatar avatar-sm" role="img" aria-label="Profile photo of Martin Hale"></div>
            <div class="author"><div class="author-name">Martin Hale</div><div class="author-scope">Public</div></div>
            <div class="post-subject">Post Subject Message</div>
            <div class="post-time"><svg viewBox="0 0 12 12"><circle cx="6" cy="6" r="5"/><path d="M6 3v3l2 1"/></svg>Today, 1:43</div>
          </div>
          <p class="post-body">Lorem ipsum dolor sit amet, paulo soleat ex sed. Discere perpetua tincidunt mel ea, mel vocent dissentiunt ut, duis aeque mucius vis ex. Eros ipsum causae ex vis, ad eos nostrud ponderum. Ea nonumy accommodare vel, te nullam docendi theophrastus mea.<span class="read-more">Read More</span></p>
        </article>
        <article class="post">
          <div class="post-head">
            <div class="avatar avatar-sm" role="img" aria-label="Profile photo of Martin Hale"></div>
            <div class="author"><div class="author-name">Martin Hale</div><div class="author-scope">Public</div></div>
            <div class="post-subject">Post Subject Message</div>
            <div class="post-time"><svg viewBox="0 0 12 12"><circle cx="6" cy="6" r="5"/><path d="M6 3v3l2 1"/></svg>Today, 1:43</div>
          </div>
          <p class="post-body">Lorem ipsum dolor sit amet, paulo soleat ex sed. Discere perpetua tincidunt mel ea, mel vocent dissentiunt ut, duis aeque mucius vis ex. Eros ipsum causae ex vis, ad eos nostrud ponderum. Ea nonumy accommodare vel, te nullam docendi theophrastus mea.<span class="read-more">Read More</span></p>
        </article>
      </section>

      <aside class="aside">
        <div class="card">
          <div class="tabs"><div class="tab is-active">Events</div><div class="tab">Tasks</div></div>
          <div class="events">
            <div class="event event-red">
              <div class="event-title"><span class="dot"></span>Director Meeting</div>
              <div class="event-meta">18 Jan, Thu | 10:00 am - 11:00 am<br>Restaurant</div>
            </div>
            <div class="event event-blue">
              <div class="event-title"><span class="dot"></span>Free Breakfast</div>
              <div class="event-meta">18 Jan, Thu | 06:30 am - 10:00 am<br>Restaurant</div>
            </div>
            <div class="event event-blue">
              <div class="event-title"><span class="dot"></span>Daddy Daughter Night</div>
              <div class="event-meta">18 Jan, Thu | 06:30 am - 10:00 am<br>Restaurant</div>
            </div>
          </div>
          <span class="card-link">View All Events</span>
        </div>

        <h3 class="polls-title">Polls</h3>
        <div class="card poll">
          <p class="poll-q">What is your favorite entree?</p>
          <div class="poll-option is-selected">Classic Chicken Sandwich</div>
          <div class="poll-option">Chicken Strips</div>
          <span class="btn btn-vote">Submit Vote</span>
          <span class="card-link">View All Polls</span>
        </div>
      </aside>
    </div>
  </div>
</body>
</html>
```